Website Redesign for Technology Focused Investment Bank

We need a website redesign for a technology and digital media focused investment banking firm. Think modern and forward thinking yet stable and smart. We provide mergers and acquisitions advisory services to our clients. Our target market are CEO's and CFO's (senior executives) that run and operate technology firms.

Kestrel Bay Advisors - www.kestrelbayadvisors.example

We are headquartered in Los Angeles, CA. Please do NOT use the Brindle Arch for anything.

We have the content and can update the photos as well.

We are looking for a "template" website we can update and edit with ease.

A competitive firm's website is: www.dunmoregrey.example Not sure I like it but I want it to look way better then this one.

Looking for a more modern version. Not too stuffy and conservative, please. Elegant, smart, updated and progressive/modern.
Updates

Color preferences:  Blue's including matching logo color. Grey's. You can add other colors if it flows well and looks clean and nice.

Menu:  Drop Down

Open to platform...please use one that most people can use, is reasonably priced if I need to buy it, and easy to update monthly and sometimes weekly.

Please use this website as a good example of what we are looking for (or similar version of it): www.plorvex.example

Thanks!
Tobias R.

We are reviewing all submissions and will select one this week. Thank you everyone for your outstanding and creative designs you have sent us. We really appreciate it.

Thanks for everyone's hard work and creative input into our website design. We really appreciate it!

Target Market(s)

CEO's and CFO's, Entrepreneurs and Board Members of Technology Companies.

Industry/Entity Type

Investment

Font styles to use
Sans Serif

Colors
33a6d7
0492cd
0555a3
3176b5
85abd2
333333
5c5c5c
757575

Requirements
Must have
• Links to social media including Twitter, LinkedIn, Google+, Socialnet, etc.

Must try to match logo color
Should not have
• No conservative, old looking colors or background. For example, no green marble look.

```html
<!DOCTYPE html>
<html lang="en">
<head>
<meta charset="utf-8">
<title>Kestrel Bay Advisors</title>
<link rel="stylesheet" href="https://fonts.googleapis.com/css2?family=Arimo:wght@400;700&display=swap">
<style>
:root{
  --blue:#0492cd;
  --blue-link:#33a6d7;
  --blue-deep:#0555a3;
  --blue-mid:#3176b5;
  --blue-soft:#85abd2;
  --ink:#333333;
  --ink-mid:#5c5c5c;
  --ink-light:#757575;
  --dark:#2b2e31;
  --darker:#1f2123;
  --rule:#4a4d50;
  --white:#ffffff;
}
*{box-sizing:border-box;margin:0;padding:0}
html,body{width:729px;height:1200px;overflow:hidden;background:var(--white)}
body{font-family:"Arimo",Arial,sans-serif;color:var(--ink)}
.page{position:relative;width:729px;height:1200px;overflow:hidden}
a{color:var(--blue-link);text-decoration:none}

/* header */
.site-header{height:78px;position:relative}
.brand{position:absolute;left:77px;top:9px;display:flex;align-items:center;gap:8px}
.brand-mark{width:37px;height:37px;border-radius:50%;background:var(--blue-mid)}
.brand-name{font-size:11px;color:var(--blue-deep)}
.social-top{position:absolute;right:75px;top:17px;display:flex;gap:3px}
.social-top span{width:19px;height:19px;border-radius:50%;background:#b5b5b5}
.main-nav{position:absolute;left:77px;top:57px;display:flex;font-size:8.4px;color:var(--ink)}
.main-nav a{color:var(--ink);padding:0 6px;border-left:1px solid #9a9a9a;line-height:9px}
.main-nav a:first-child{padding-left:0;border-left:0;color:var(--blue-deep)}

/* hero */
.hero{position:relative;height:384px;background:linear-gradient(180deg,#3b5fb5 0%,#7a98d2 20%,#cbd8ee 33%,#9fae86 42%,#8f9a52 60%,#c7b97a 85%,#d6c48a 100%)}
.hero-title{position:absolute;top:95px;width:100%;text-align:center;color:var(--white);font-size:21px;line-height:27px;text-shadow:0 1px 3px rgba(0,0,0,.55)}
.hero-arrow{position:absolute;top:176px;width:30px;height:31px;background:var(--blue)}
.hero-arrow svg{display:block;margin:10px auto}
.hero-arrow.prev{left:0}.hero-arrow.next{right:0}

/* sectors */
.sectors{height:238px;text-align:center}
.sectors h2{font-weight:400;font-size:21px;color:var(--ink-mid);padding-top:20px}
.sector-list{display:flex;justify-content:center;gap:52px;margin-top:23px;margin-left:-4px}
.sector{width:136px}
.sector-icon{width:58px;height:58px;border-radius:50%;margin:0 auto;background:radial-gradient(circle at 40% 35%,#bfe4fb,#1f7fd0 60%,#0d3f8e)}
.sector h3{font-weight:400;font-size:14px;color:var(--ink-mid);margin-top:10px}
.sector p{font-size:8px;line-height:9.5px;color:var(--ink-mid);margin-top:9px}

/* footer columns */
.info{height:458px;background:var(--dark);color:#c9c9c9;display:flex;padding:48px 0 0 77px;font-size:8px;line-height:10px}
.info h4{font-weight:400;font-size:13.5px;color:#d9d9d9;margin-bottom:12px}
.col-why{width:145px}
.col-services{width:150px}
.col-news{width:149px}
.col-tweets{width:131px}
.why-photo{width:128px;height:96px;border:1px solid #8a8a8a;background:linear-gradient(180deg,#c7d0d8,#5b6670 60%,#2d3338);margin-bottom:19px}
.info p{margin-bottom:9px}
.service-list{list-style:none;margin-bottom:23px}
.service-list li{display:flex;gap:4px;margin-bottom:9px}
.service-list svg{flex:none;margin-top:1px}
.news-item{border-bottom:1px dotted #6b6b6b;padding-bottom:9px;margin-bottom:17px}
.news-date{font-style:italic;font-size:7px;color:#9a9a9a;margin-bottom:8px}
.news-title{color:var(--blue-link);margin-bottom:7px;font-size:8.4px}
.view-all{color:var(--blue-link)}
.tweets-head{display:flex;align-items:center;justify-content:space-between}
.follow-btn{font-size:8px;background:#e9eef2;color:var(--ink);border:1px solid #aab;padding:1px 5px;margin-bottom:12px}
.tweet-box{width:131px;height:331px;background:var(--darker);border:1px solid #3d4044;position:relative;padding:3px 16px 0 3px;overflow:hidden}
.tweet-scroll{position:absolute;right:1px;top:1px;bottom:1px;width:11px;background:#cfd8e4}
.tweet-scroll i{position:absolute;left:1px;right:1px;top:14px;height:14px;background:#7f9dc7}
.tweet-meta{display:flex;gap:4px;font-size:7px;line-height:8px;margin-bottom:5px}
.tweet-avatar{width:15px;height:15px;border-radius:50%;background:var(--blue-soft);flex:none}
.tweet-meta em{color:var(--blue-link)}
.tweet-date{margin-left:auto;color:var(--blue-link);font-style:italic}
.tweet-text{margin-bottom:3px}
.tweet-photo{height:45px;margin-bottom:3px}
.tweet-photo.one{background:linear-gradient(90deg,#3c4a52,#8fa7a0 55%,#2a8a54)}
.tweet-photo.two{background:linear-gradient(90deg,#0e3c3a,#2b6a62,#113030)}
.tweet-link{color:var(--blue-link)}
.tweet-sep{border-top:1px dotted #6b6b6b;margin:3px 0 6px}

/* bottom bar */
.legal{height:42px;background:var(--darker);display:flex;align-items:center;justify-content:space-between;padding:0 75px 0 77px;font-size:6.5px;color:#bdbdbd}
.social-bottom{display:flex;gap:8px}
.social-bottom span{width:11px;height:11px;background:#bdbdbd}
</style>
</head>
<body>
<div class="page">
  <header class="site-header">
    <div class="brand"><span class="brand-mark"></span><span class="brand-name">Kestrel Bay Advisors</span></div>
    <div class="social-top" aria-label="Social media links"><span></span><span></span><span></span><span></span></div>
    <nav class="main-nav">
      <a>Home</a><a>About Us</a><a>Services</a><a>Transactions</a><a>Research</a><a>Private Equity</a><a>Recommendations</a><a>About the Founder</a><a>Careers</a><a>News+Blog</a><a>Contact Us</a>
    </nav>
  </header>

  <section class="hero" role="img" aria-label="Two dark horses meeting in a grassy meadow under a blue sky">
    <h1 class="hero-title" style="font-weight:400">We are Technology and Digital Media Industry<br>Mergers &amp; Acquisitions Experts</h1>
    <span class="hero-arrow prev"><svg width="8" height="11" viewBox="0 0 8 11"><path d="M6 1 2 5.5 6 10" stroke="#fff" stroke-width="2" fill="none"/></svg></span>
    <span class="hero-arrow next"><svg width="8" height="11" viewBox="0 0 8 11"><path d="M2 1 6 5.5 2 10" stroke="#fff" stroke-width="2" fill="none"/></svg></span>
  </section>

  <section class="sectors">
    <h2>Industry Sectors We Cover</h2>
    <div class="sector-list">
      <div class="sector"><div class="sector-icon" role="img" aria-label="Globe with a gear"></div><h3>Software</h3><p>Our professionals are able to assist with complex strategic and financial M&amp;A transactions within the software industry. <a>Read more [...]</a></p></div>
      <div class="sector"><div class="sector-icon" role="img" aria-label="Globe of connected nodes"></div><h3>IT Services</h3><p>We provide investment banking and M&amp;A advisory services to some of the largest IT Services firms across the globe. <a>Read more [...]</a></p></div>
      <div class="sector"><div class="sector-icon" role="img" aria-label="Globe with a stethoscope"></div><h3>Internet &amp; Digital media</h3><p>We provide investment banking and M&amp;A advisory services to some of the largest Internet and Digital Media firms across the globe. <a>Read more [...]</a></p></div>
    </div>
  </section>

  <section class="info">
    <div class="col-why">
      <h4>Why Us?</h4>
      <div class="why-photo" role="img" aria-label="Modern office lounge interior"></div>
      <p>We are an independent investment bank and M&amp;A advisory firm focused exclusively on the global Technology and Digital Media sectors. Specifically, we execute mergers and acquisitions for the Software, IT Services, Internet and Digital Media industry sectors.</p>
      <p>Our professionals have completed over $20 billion in transactions to date and have experience in investment banking, private equity and capital markets from leading firms. We are experts in complex M&amp;A transactions of most shapes and sizes and have deep industry expertise.</p>
    </div>
    <div class="col-services">
      <h4>Services Provided</h4>
      <ul class="service-list">
        <li><svg width="8" height="7" viewBox="0 0 8 7"><path d="M1 3.5 3 5.5 7 1" stroke="var(--blue-link)" stroke-width="1.6" fill="none"/></svg>Buy-Side Mergers and Acquisitions</li>
        <li><svg width="8" height="7" viewBox="0 0 8 7"><path d="M1 3.5 3 5.5 7 1" stroke="var(--blue-link)" stroke-width="1.6" fill="none"/></svg>Sell-Side Mergers and Acquisitions</li>
        <li><svg width="8" height="7" viewBox="0 0 8 7"><path d="M1 3.5 3 5.5 7 1" stroke="var(--blue-link)" stroke-width="1.6" fill="none"/></svg>Recapitalizations and Restructuring's</li>
        <li><svg width="8" height="7" viewBox="0 0 8 7"><path d="M1 3.5 3 5.5 7 1" stroke="var(--blue-link)" stroke-width="1.6" fill="none"/></svg>Equity and Debt Buyout Financing (Advisory)</li>
        <li><svg width="8" height="7" viewBox="0 0 8 7"><path d="M1 3.5 3 5.5 7 1" stroke="var(--blue-link)" stroke-width="1.6" fill="none"/></svg>Spin-Offs and Asset Sales</li>
        <li><svg width="8" height="7" viewBox="0 0 8 7"><path d="M1 3.5 3 5.5 7 1" stroke="var(--blue-link)" stroke-width="1.6" fill="none"/></svg>Strategic and Corporate Finance Advisory</li>
        <li><svg width="8" height="7" viewBox="0 0 8 7"><path d="M1 3.5 3 5.5 7 1" stroke="var(--blue-link)" stroke-width="1.6" fill="none"/></svg>Fairness Opinions and Valuations</li>
      </ul>
      <p>M&amp;A is the foundation and focus of our firm.</p>
      <p>Our services include evaluating potential targets or merger partners, providing valuation analyses, and evaluating and proposing financial and strategic alternatives.</p>
      <p>We advise on strategy, timing, structure, financing, and pricing, and assist in negotiating and closing M&amp;A transactions.</p>
      <p>Our professionals have completed over $20 billion in M&amp;A transactions and are seasoned experts with deep technology industry experience.</p>
    </div>
    <div class="col-news">
      <h4>News and Blog</h4>
      <div class="news-item">
        <div class="news-date">Fri, Feb 14 2014 - 12:04 AM</div>
        <div class="news-title">Technology Mergers on Upswing in Q1 2014</div>
        <p>2014 is off to a strong start for technology M&amp;A announcements. We noted a number of new transactions announced in January and early February 2014. According to several M&amp;A research reports and survey <a>Read More [...]</a></p>
      </div>
      <div class="news-item">
        <div class="news-date">Thu, May 23 2013 - 5:44 PM</div>
        <div class="news-title">Devan Mehra will be a speaker at the Mobile Venue Expo - The Mobile...</div>
        <p>Devan Mehra, Managing Director at Kestrel Bay Advisors, will be speaking at the 2013 Mobile Venue Expo - The Mobile Summit for Hospitality and Retail held in Las Vegas, NV on May 23, 2013 at The <a>Read More [...]</a></p>
      </div>
      <a class="view-all">View All ›</a>
    </div>
    <div class="col-tweets">
      <div class="tweets-head"><h4>Latest tweets</h4><span class="follow-btn">Follow</span></div>
      <div class="tweet-box">
        <div class="tweet-scroll"><i></i></div>
        <div class="tweet-meta"><span class="tweet-avatar"></span><span>Kestrel Bay<br><em>@KestrelBayMA</em></span><span class="tweet-date">21 FEB</span></div>
        <p class="tweet-text">M&amp;A - Best Start to Year Since 2011 <a class="tweet-link">lnk.example/a1</a></p>
        <div class="tweet-photo one" role="img" aria-label="Person walking past a branded van"></div>
        <p class="tweet-text"><a class="tweet-link">M&amp;A — Best Start to Year Since 2011 - MarketPulse - Ledger</a></p>
        <p class="tweet-text">It's been a shaky start to the year in the global stock and currency markets, but dealmakers don't seem to mind. In January 2014, companies and funds inked $228.2 billion in global deals M&amp;A, the...</p>
        <div class="tweet-sep"></div>
        <div class="tweet-meta"><span class="tweet-avatar"></span><span>Kestrel Bay<br><em>@KestrelBayMA</em></span><span class="tweet-date">21 FEB</span></div>
        <p class="tweet-text">Socialnet acquires ChatLine messaging service for $16 billion <a class="tweet-link">lnk.example/b2</a></p>
        <div class="tweet-photo two" role="img" aria-label="Smartphone showing a messaging app"></div>
        <p class="tweet-text"><a class="tweet-link">M&amp;A — Best Start to Year Since 2011 - MarketPulse - Ledger</a></p>
      </div>
    </div>
  </section>

  <footer class="legal">
    <span>Copyright 2014 <a>Kestrel Bay Advisors, LLC</a> - All Rights Reserved</span>
    <div class="social-bottom" aria-label="Social media links"><span></span><span></span><span></span><span></span></div>
  </footer>
</div>
</body>
</html>
```